Funky new Serviced Apartment Company needs a website + logo

Bright Nest Serviced Accommodation is a new company aiming to attract customers who need temporary accommodation (2 days to 6 months) in city locations.

Our customers make considerable savings on longer stays compared to hotels, and have all the creature comforts of home including super-fast WIFI, comfy beds, full kitchen and modern, yet comfortable, furniture.

Another key feature of the design is a page to attract "Partners" who "Work with Us" by allowing us to manage their properties and becoming part of our network of accommodation units. I have include a brochure from one of our competitors, and a video can be found here: http://lnkvault-example.com/aptclip-7 - both can be used as I have permission.

The website design should work on all devices and screen sizes, and lend itself to a mobile app.

We would like to see website designs that are modern and simple, with a strong brand logo. The final design should communicate "Home From Home" and aim to attract professionals away from home on business for long periods of time.

Target Market(s)

Professional People working away from home for extended periods of time

Industry/Entity Type

Accommodation

Contact Information for Business Card

Name, Title, Phone Number, Email
Callum Fenwick, Owner, 07831 552907, callum.fenwick@brightnestsa-example.co.uk

Logo Text

Bright Nest Service Accommodation (Serviced Accommodation optional)

Coding

Coded - Design and coding required

Number of Pages Required

3 page

Font styles to use
Sans Serif

Requirements
Must have
• A 3 page website: Home, Partners, Contact Us
• Home page should have an area to list current apartment units, the user should be able to select a location and filter the list based on price and number of people.
• Partners page should inspire a "Work with us" call to action.
• The design should work with all screen sizes and devices.
• The design should say friendly and professional
Nice to have
• A simple logo, perhaps a smiling face made up using letters 'W' and 'H'.
• A neutral color scheme
Should not have
• No garish or vivid color scheme

```html
<!DOCTYPE html>
<html lang="en">
<head>
<meta charset="utf-8">
<title>Bright Nest Serviced Accommodation</title>
<link href="https://fonts.googleapis.com/css2?family=Lato:wght@300;400;700;900&family=Raleway:wght@500;600&display=swap" rel="stylesheet">
<style>
:root{
  --navy:#1f3447;
  --navy-deep:#172939;
  --footer:#22394e;
  --bar:#1a2c3c;
  --muted:#9fb1c2;
  --text:#2b2f33;
  --line:#d4d9de;
  --field:#c9d3dc;
  --star:#f2b632;
  --white:#ffffff;
}
*{margin:0;padding:0;box-sizing:border-box}
html,body{width:1200px;height:3429px;overflow:hidden}
body{position:relative;background:var(--white);font-family:'Lato',sans-serif;color:var(--text)}
.abs{position:absolute}

/* header */
.topbar{left:0;top:0;width:1200px;height:32px;background:var(--navy)}
.site-header{left:0;top:32px;width:1200px;height:98px;background:var(--white)}
.brand{left:121px;top:52px;display:flex;align-items:center;gap:14px}
.brand-dot{width:54px;height:54px;border-radius:50%;background:var(--navy)}
.brand-name{font-weight:900;font-size:22px;color:var(--navy);line-height:1.1;letter-spacing:.5px}
.brand-name small{display:block;font-weight:700;font-size:12px;color:var(--navy);letter-spacing:.8px}
.nav{top:86px;font-size:14px;font-weight:700;letter-spacing:.5px;color:var(--muted)}
.nav.active{color:var(--navy);border-bottom:2px solid var(--navy);padding-bottom:4px}

/* hero */
.hero{left:0;top:130px;width:1200px;height:499px;background:linear-gradient(180deg,#cfdde3 0%,#e6dfd0 38%,#d8c19a 70%,#c9a877 100%)}
.hero-title{left:151px;top:462px;font-size:50px;color:var(--navy);font-weight:300;letter-spacing:-.5px}
.hero-title b{font-weight:900}
.hero-arrow{top:340px}

/* section headings */
.section-title{left:121px;font-size:17px;font-weight:900;color:var(--navy);letter-spacing:.3px}
.section-rule{height:1px;background:var(--line)}

/* search */
.search-sub{left:121px;top:738px;font-size:13px;color:var(--muted);font-weight:700}
.field{top:775px;height:42px;border:1px solid var(--field);padding:6px 8px}
.field span{display:block;font-size:9px;color:#7c8a96}
.field em{display:block;font-style:normal;font-size:10px;color:#4b5863;margin-top:4px}
.search-btn{left:974px;top:780px;width:105px;height:32px;background:var(--navy);color:var(--white);font-size:11px;font-weight:700;display:flex;align-items:center;justify-content:flex-end;padding-right:22px}
.btn-dot{left:964px;top:774px;width:40px;height:40px;border-radius:50%;background:var(--white);border:3px solid var(--navy)}

/* homes */
.home-card{width:222px}
.home-photo{position:relative;width:222px;height:294px;overflow:hidden}
.price-tag{position:absolute;right:0;top:0;width:0;height:0;border-top:58px solid var(--navy);border-left:58px solid transparent}
.price-tag i{position:absolute;right:2px;top:-50px;transform:rotate(45deg);font-style:normal;color:var(--white);font-size:11px;font-weight:700}
.home-caption{font-size:11.5px;margin-top:10px;color:var(--text)}

/* why choose us */
.why-panel{left:121px;top:2199px;width:958px;height:112px;border:1px solid #b9c3cc;border-radius:14px}
.why-item{width:150px;text-align:center;top:2167px}
.why-icon{width:74px;height:74px;border-radius:50%;background:var(--navy);margin:0 auto;display:flex;align-items:center;justify-content:center;border:4px solid var(--white);box-shadow:0 0 0 1px #b9c3cc}
.why-label{font-size:12px;line-height:1.4;margin-top:10px;color:var(--text)}

/* customers band */
.band{left:0;top:2371px;width:1200px;height:247px;background:linear-gradient(100deg,#4c5c6a 0%,#62717d 45%,#3e4e5c 100%)}
.band-shade{left:0;top:2371px;width:1200px;height:247px;background:rgba(31,52,71,.45)}
.band-title{left:121px;top:2428px;font-size:40px;color:var(--white);font-weight:400;letter-spacing:.5px}
.band-title b{font-weight:900;font-size:54px}
.contact-btn{left:121px;top:2522px;width:200px;height:30px;background:var(--navy);color:var(--white);font-size:11px;font-weight:700;display:flex;align-items:center;padding-left:54px;gap:8px}
.contact-dot{left:113px;top:2516px;width:42px;height:42px;border-radius:50%;background:#3b5066;border:3px solid var(--white)}

/* reviews */
.avatar{left:119px;top:2775px;width:114px;height:114px;border-radius:50%;background:linear-gradient(160deg,#d6d9dc,#8f969c);border:4px solid var(--white);box-shadow:0 0 0 2px var(--navy)}
.review-text{left:258px;top:2782px;width:821px;font-size:12.5px;font-style:italic;line-height:1.6;color:var(--text)}
.reviewer{left:258px;top:2878px;font-size:18px;font-weight:900;font-style:italic;color:var(--navy)}
.stars{left:258px;top:2906px;color:var(--star);font-size:12px;letter-spacing:2px}
.dots{left:165px;top:2914px;display:flex;gap:5px}
.dots i{width:7px;height:7px;border-radius:50%;background:#b8c0c7}
.dots i:first-child{background:var(--navy)}

/* newsletter */
.newsletter{left:0;top:2985px;width:1200px;height:78px;background:var(--navy-deep)}
.nl-dot{left:121px;top:3009px;width:30px;height:30px;border-radius:50%;background:#3b5066}
.nl-title{left:198px;top:3004px;font-family:'Raleway',sans-serif;font-weight:600;font-size:28px;color:var(--white)}
.nl-input{left:514px;top:3008px;width:382px;height:32px;background:var(--white);font-size:11px;color:#7c8a96;padding:9px 12px}
.nl-btn{left:922px;top:3006px;width:155px;height:36px;border:1px solid #4a6077;color:var(--white);font-size:12px;font-weight:700;display:flex;align-items:center;justify-content:flex-end;padding-right:22px}
.nl-btn-dot{left:916px;top:3005px;width:38px;height:38px;border-radius:50%;background:#3b5066}

/* footer */
.footer{left:0;top:3063px;width:1200px;height:320px;background:var(--footer);color:var(--white)}
.f-title{font-size:12px;font-weight:900;letter-spacing:.5px;top:3127px}
.f-links{left:121px;top:3162px;font-size:11px;line-height:40px;list-style:none}
.f-links li::before{content:"›";margin-right:12px;color:var(--muted)}
.f-info{left:288px;top:3160px;font-size:11px;line-height:1.55;width:250px}
.f-row{display:flex;gap:12px;margin-bottom:16px;align-items:flex-start}
.f-row b{font-weight:700}
.f-row.big{font-size:15px}
.f-input{left:587px;width:236px;background:var(--field);font-size:10px;color:#5c6a76;padding:6px 8px}
.f-submit{left:598px;top:3289px;width:126px;height:30px;border:1px solid #4a6077;font-size:11px;font-weight:700;display:flex;align-items:center;justify-content:flex-end;padding-right:26px}
.f-submit-dot{left:587px;top:3285px;width:38px;height:38px;border-radius:50%;background:#3b5066}
.f-brand{left:906px;top:3178px;width:178px;text-align:center}
.f-brand-dot{width:78px;height:78px;border-radius:50%;border:5px solid #c5ced6;margin:0 auto 14px}
.f-brand-name{font-weight:900;font-size:18px;color:#c5ced6;letter-spacing:1px}

.bottom{left:0;top:3383px;width:1200px;height:46px;background:var(--bar)}
.copyright{left:121px;top:3399px;font-size:11px;color:var(--white)}
.social{top:3395px;width:23px;height:23px;border-radius:50%;background:var(--white)}
</style>
</head>
<body>

<!-- header -->
<div class="abs topbar"></div>
<header class="abs site-header"></header>
<div class="abs brand">
  <span class="brand-dot"></span>
  <span class="brand-name">BRIGHT NEST<small>SERVICED ACCOMMODATION</small></span>
</div>
<a class="abs nav active" style="left:783px">HOME</a>
<a class="abs nav" style="left:884px">PARTNERS</a>
<a class="abs nav" style="left:1003px">CONTACT US</a>

<!-- hero -->
<div class="abs hero" role="img" aria-label="Small white model house with a red roof resting on a sunlit sandy beach"></div>
<h1 class="abs hero-title"><b>Home away</b> from Home</h1>
<svg class="abs hero-arrow" style="left:86px" width="30" height="64" viewBox="0 0 30 64"><polyline points="26,2 4,32 26,62" fill="none" stroke="#1f3447" stroke-width="4"/></svg>
<svg class="abs hero-arrow" style="left:1084px" width="30" height="64" viewBox="0 0 30 64"><polyline points="4,2 26,32 4,62" fill="none" stroke="#1f3447" stroke-width="4"/></svg>

<!-- search -->
<h2 class="abs section-title" style="top:703px">BRIGHT NEST SERVICED ACCOMMODATION</h2>
<div class="abs section-rule" style="left:546px;top:722px;width:533px"></div>
<p class="abs search-sub">Book Unique Home And Experience A City Like A Local.</p>
<div class="abs field" style="left:121px;width:252px"><span>Where</span><em>Anywhere</em></div>
<div class="abs field" style="left:405px;width:251px"><span>When</span><em>Anytime</em></div>
<div class="abs field" style="left:688px;width:252px"><span>Guests</span><em>1 Guest &#8964;</em></div>
<div class="abs search-btn">Search</div>
<div class="abs btn-dot"></div>

<!-- homes -->
<h2 class="abs section-title" style="top:893px">HOMES</h2>
<div class="abs section-rule" style="left:190px;top:911px;width:889px"></div>

<div class="abs home-card" style="left:121px;top:946px"><div class="home-photo" role="img" aria-label="Bright living room with grey sofa and wooden floor" style="background:linear-gradient(160deg,#f1f1ef,#b9a58b 70%,#8a7a66)"><span class="price-tag"><i>$180</i></span></div><p class="home-caption">Lorem ipsum dolor sit amet, consect</p></div>
<div class="abs home-card" style="left:366px;top:946px"><div class="home-photo" role="img" aria-label="Dining area by tall windows with blinds" style="background:linear-gradient(170deg,#e9ebec,#a9a6a1 60%,#6b5340)"><span class="price-tag"><i>$180</i></span></div><p class="home-caption">Lorem ipsum dolor sit amet, consect</p></div>
<div class="abs home-card" style="left:610px;top:946px"><div class="home-photo" role="img" aria-label="Lounge with orange feature wall and wall-mounted TV" style="background:linear-gradient(170deg,#e6a52a,#d89826 45%,#8c5a35)"><span class="price-tag"><i>$180</i></span></div><p class="home-caption">Lorem ipsum dolor sit amet, consect</p></div>
<div class="abs home-card" style="left:855px;top:946px"><div class="home-photo" role="img" aria-label="Pale green sitting room with sea view" style="background:linear-gradient(170deg,#c9dcd6,#b7c8c2 55%,#9a8e7c)"><span class="price-tag"><i>$180</i></span></div><p class="home-caption">Lorem ipsum dolor sit amet, consect</p></div>

<div class="abs home-card" style="left:121px;top:1312px"><div class="home-photo" role="img" aria-label="Modern bathroom with freestanding bath" style="background:linear-gradient(170deg,#8f8d89,#c9c6c1 55%,#e9e7e3)"><span class="price-tag"><i>$180</i></span></div><p class="home-caption">Lorem ipsum dolor sit amet, consect</p></div>
<div class="abs home-card" style="left:366px;top:1312px"><div class="home-photo" role="img" aria-label="Kitchen opening onto a green garden" style="background:linear-gradient(170deg,#6f8a52,#c8cdc7 50%,#2d2f31)"><span class="price-tag"><i>$180</i></span></div><p class="home-caption">Lorem ipsum dolor sit amet, consect</p></div>
<div class="abs home-card" style="left:610px;top:1312px"><div class="home-photo" role="img" aria-label="Open living room with fireplace and large windows" style="background:linear-gradient(170deg,#f2f2f0,#d4d0c8 55%,#8a7d6c)"><span class="price-tag"><i>$180</i></span></div><p class="home-caption">Lorem ipsum dolor sit amet, consect</p></div>
<div class="abs home-card" style="left:855px;top:1312px"><div class="home-photo" role="img" aria-label="Living room with grey sofa and shelving" style="background:linear-gradient(160deg,#eceeee,#bfae96 70%,#857460)"><span class="price-tag"><i>$180</i></span></div><p class="home-caption">Lorem ipsum dolor sit amet, consect</p></div>

<div class="abs home-card" style="left:121px;top:1682px"><div class="home-photo" role="img" aria-label="White wardrobe shelves with wicker baskets" style="background:linear-gradient(170deg,#f4f3f0,#d9d3c6 55%,#a6895f)"><span class="price-tag"><i>$180</i></span></div><p class="home-caption">Lorem ipsum dolor sit amet, consect</p></div>
<div class="abs home-card" style="left:366px;top:1682px"><div class="home-photo" role="img" aria-label="Dark wood kitchen with island and pendant lights" style="background:linear-gradient(170deg,#4a3a2e,#7a6550 50%,#2a211b)"><span class="price-tag"><i>$180</i></span></div><p class="home-caption">Lorem ipsum dolor sit amet, consect</p></div>
<div class="abs home-card" style="left:610px;top:1682px"><div class="home-photo" role="img" aria-label="Sunny room with glass table and ocean view" style="background:linear-gradient(170deg,#bcd8ea,#e9eef0 55%,#c9c3b6)"><span class="price-tag"><i>$180</i></span></div><p class="home-caption">Lorem ipsum dolor sit amet, consect</p></div>
<div class="abs home-card" style="left:855px;top:1682px"><div class="home-photo" role="img" aria-label="Bedroom with grey bedding and orange cushions" style="background:linear-gradient(170deg,#f1efeb,#cfcac3 55%,#9a948c)"><span class="price-tag"><i>$180</i></span></div><p class="home-caption">Lorem ipsum dolor sit amet, consect</p></div>

<!-- why choose us -->
<h2 class="abs section-title" style="top:2093px">WHY CHOOSE US</h2>
<div class="abs section-rule" style="left:290px;top:2111px;width:789px"></div>
<div class="abs why-panel"></div>

<div class="abs why-item" style="left:117px">
  <div class="why-icon"><svg width="34" height="34" viewBox="0 0 34 34" fill="none" stroke="#fff" stroke-width="2"><rect x="4" y="7" width="26" height="22" rx="2"/><line x1="4" y1="13" x2="30" y2="13"/><line x1="10" y1="4" x2="10" y2="9"/><line x1="24" y1="4" x2="24" y2="9"/><polyline points="11,21 15,25 23,17"/></svg></div>
  <p class="why-label">Regular bookings,<br>regular payments</p>
</div>
<div class="abs why-item" style="left:279px">
  <div class="why-icon"><svg width="34" height="34" viewBox="0 0 34 34" fill="none" stroke="#fff" stroke-width="2"><circle cx="17" cy="11" r="6"/><path d="M5 30c0-7 5-11 12-11s12 4 12 11"/></svg></div>
  <p class="why-label">Managing your<br>bookings</p>
</div>
<div class="abs why-item" style="left:442px">
  <div class="why-icon"><svg width="34" height="34" viewBox="0 0 34 34" fill="none" stroke="#fff" stroke-width="2"><path d="M4 6h20v13H12l-6 5v-5H4z"/><path d="M27 12h3v12h-2v4l-5-4h-8v-3"/></svg></div>
  <p class="why-label">Expert support<br>from the start</p>
</div>
<div class="abs why-item" style="left:604px">
  <div class="why-icon"><svg width="34" height="34" viewBox="0 0 34 34" fill="none" stroke="#fff" stroke-width="2"><path d="M17 3v28"/><path d="M23 9c-1-3-4-4-6-4-4 0-6 2-6 5 0 6 12 4 12 10 0 3-2 5-6 5-3 0-6-1-7-4"/></svg></div>
  <p class="why-label">Maximise your<br>income</p>
</div>
<div class="abs why-item" style="left:766px">
  <div class="why-icon"><svg width="34" height="34" viewBox="0 0 34 34" fill="none" stroke="#fff" stroke-width="2.4"><polyline points="6,18 14,26 28,8"/></svg></div>
  <p class="why-label">You'll be in<br>control</p>
</div>
<div class="abs why-item" style="left:933px">
  <div class="why-icon"><svg width="34" height="34" viewBox="0 0 34 34" fill="none" stroke="#fff" stroke-width="2"><path d="M17 29S4 21 4 12a6.5 6.5 0 0 1 13-2 6.5 6.5 0 0 1 13 2c0 9-13 17-13 17z"/></svg></div>
  <p class="why-label">Your peace<br>of mind</p>
</div>

<!-- customers band -->
<div class="abs band" role="img" aria-label="Apartment interior where a couple receive keys from an agent"></div>
<div class="abs band-shade"></div>
<h2 class="abs band-title">MORE THEN <b>2000</b> HAPPY CUSTOMERS</h2>
<div class="abs contact-btn">CONTACT TODAY <svg width="18" height="10" viewBox="0 0 18 10"><path d="M0 5h15M11 1l5 4-5 4" stroke="#fff" stroke-width="2" fill="none"/></svg></div>
<div class="abs contact-dot"></div>

<!-- reviews -->
<h2 class="abs section-title" style="top:2694px">CUSTOMER REVIEWS</h2>
<div class="abs section-rule" style="left:320px;top:2712px;width:759px"></div>
<div class="abs avatar" role="img" aria-label="Portrait of a smiling customer"></div>
<p class="abs review-text">Lorem ipsum dolor sit amet, consectetuer adipiscing elit, sed diam nonummy nibh euismod tincidunt ut laoreet dolore magna aliquam erat volutpat. Ut wisi enim ad minim veniam, quis nostrud exerci tation ullamcorper suscipit lobortis nisl ut aliquip ex ea commodo consequat. Duis autem vel eum iriure dolor in hendrerit in vulputate Ut wisi enim ad minim veniam, quis nostrud exerci tation nisl ut aliquip ex ea commodo</p>
<p class="abs reviewer">- Mr. Tobias Marlow</p>
<p class="abs stars">★★★★★</p>
<div class="abs dots"><i></i><i></i><i></i></div>

<!-- newsletter -->
<div class="abs newsletter"></div>
<div class="abs nl-dot"></div>
<p class="abs nl-title">Newsletter Signup</p>
<svg class="abs" style="left:464px;top:3004px" width="20" height="40" viewBox="0 0 20 40"><polyline points="3,2 17,20 3,38" fill="none" stroke="#9fb1c2" stroke-width="2"/></svg>
<div class="abs nl-input">Email</div>
<div class="abs nl-btn">SUBSCRIBE</div>
<div class="abs nl-btn-dot"></div>

<!-- footer -->
<footer class="abs footer"></footer>
<p class="abs f-title" style="left:121px;color:#fff">QUICK LINKS</p>
<ul class="abs f-links" style="color:#fff"><li>Home</li><li>Partners</li><li>Contact Us</li></ul>

<p class="abs f-title" style="left:288px;color:#fff">CONTACT INFORMATION</p>
<div class="abs f-info" style="color:#fff">
  <div class="f-row"><svg width="14" height="20" viewBox="0 0 14 20"><path d="M7 0a7 7 0 0 0-7 7c0 5 7 13 7 13s7-8 7-13a7 7 0 0 0-7-7zm0 10a3 3 0 1 1 0-6 3 3 0 0 1 0 6z" fill="#fff"/></svg><span><b>Bright Nest Serviced Accommodation</b><br>218 Harbour Row,<br>Ashford Vale, KT 40912</span></div>
  <div class="f-row big"><svg width="14" height="14" viewBox="0 0 24 24"><path d="M6.6 10.8a15 15 0 0 0 6.6 6.6l2.2-2.2a1 1 0 0 1 1-.25 11.4 11.4 0 0 0 3.6.6 1 1 0 0 1 1 1V20a1 1 0 0 1-1 1A17 17 0 0 1 3 4a1 1 0 0 1 1-1h3.5a1 1 0 0 1 1 1c0 1.3.2 2.5.6 3.6a1 1 0 0 1-.25 1z" fill="#fff"/></svg><span>0161 555 0198</span></div>
  <div class="f-row big"><svg width="14" height="14" viewBox="0 0 24 24"><rect x="3" y="3" width="18" height="18" rx="2" fill="none" stroke="#fff" stroke-width="2"/><line x1="7" y1="9" x2="17" y2="9" stroke="#fff" stroke-width="2"/><line x1="7" y1="14" x2="17" y2="14" stroke="#fff" stroke-width="2"/></svg><span>0161 555 0198</span></div>
  <div class="f-row"><svg width="14" height="12" viewBox="0 0 24 18"><rect x="1" y="1" width="22" height="16" fill="none" stroke="#fff" stroke-width="2"/><polyline points="1,1 12,10 23,1" fill="none" stroke="#fff" stroke-width="2"/></svg><span>info@brightnestsa-example.co.uk</span></div>
</div>

<p class="abs f-title" style="left:587px;color:#fff">QUICK CONTACT</p>
<div class="abs f-input" style="top:3162px;height:26px">Your name</div>
<div class="abs f-input" style="top:3197px;height:26px">Your e-mail</div>
<div class="abs f-input" style="top:3232px;height:50px">Your message</div>
<div class="abs f-submit" style="color:#fff">SUBMIT</div>
<div class="abs f-submit-dot"></div>

<div class="abs f-brand"><div class="f-brand-dot"></div><p class="f-brand-name">BRIGHT NEST</p></div>

<div class="abs bottom"></div>
<p class="abs copyright">© 2017 Bright Nest Serviced Accommodation . All Rights Reserved</p>
<span class="abs social" style="left:926px"></span>
<span class="abs social" style="left:965px"></span>
<span class="abs social" style="left:1014px"></span>
<span class="abs social" style="left:1055px"></span>

</body>
</html>
```